Real estate business card

I need a business card for my real estate company. I help clients buy and sell properties. I would like to keep the design very simple and professional. I would like the design to convey professionalism, safety and trust. I prefer no graphics but a simple logo design would be nice if that is part of what you do.
Updates

Please keep the designs simple. No high-rise buildings please. 

Target Market(s)

Age group 30-60 mostly affluent

Industry/Entity Type

Real Estate

Contact Information for Business Card

Venkell Realtors
Bernard Venkell, Broker
5146 Marrow Ave. #327, La Crescenta, CA 91214

Requirements
Nice to have
• Logo can be combination of my initials BV or just Z or a simple geometric shape? Please see "Desig Ideas" attachment. No pics of houses or shaking hands, dollar bills, $, %, etc...
Please use fonts similar to Helvetica for a clean, modern look (think Northern European design, simple, clean yet bold)

Also use font colors such as blue, grey in different shades. Use pastel colors if better.

```html
<!DOCTYPE html>
<html lang="en">
<head>
<meta charset="utf-8">
<title>Venkell Realtors – Business Card</title>
<link href="https://fonts.googleapis.com/css2?family=Arimo:wght@400&display=swap" rel="stylesheet">
<style>
  :root {
    --page-bg: #f3fbfd;
    --card-bg: #ffffff;
    --card-edge: #2b2b2b;
    --card-shadow: #cfd3d6;
    --accent-cyan: #1cc6ef;
    --brand-blue: #0b6dc7;
    --text-dark: #444444;
    --text-mid: #555555;
    --text-soft: #8a8a8a;
    --divider: #b5b5b5;
    --white: #ffffff;
  }
  html, body {
    margin: 0;
    padding: 0;
    overflow: hidden;
  }
  body {
    font-family: "Arimo", Helvetica, Arial, sans-serif;
  }
  .canvas {
    position: relative;
    width: 1200px;
    height: 927px;
    background: var(--page-bg);
    overflow: hidden;
  }

  /* Business card */
  .card {
    position: absolute;
    left: 133px;
    top: 111px;
    width: 735px;
    height: 461px;
    background: var(--card-bg);
    border: 1px solid var(--card-edge);
    border-radius: 24px;
    box-shadow: 10px 10px 0 var(--card-shadow);
    overflow: hidden;
    box-sizing: border-box;
  }
  .brand {
    position: absolute;
    left: 0;
    right: 0;
    top: 134px;
    display: flex;
    justify-content: center;
    align-items: center;
    gap: 10px;
  }
  .brand-mark {
    width: 16px;
    height: 16px;
    background: var(--accent-cyan);
  }
  .brand-name {
    font-size: 27px;
    line-height: 1;
    color: var(--text-mid);
  }
  .rule {
    position: absolute;
    left: 29px;
    right: 27px;
    top: 175px;
    height: 3px;
    background: var(--accent-cyan);
  }
  .address {
    position: absolute;
    left: 0;
    right: 0;
    top: 182px;
    margin: 0;
    text-align: center;
    font-size: 17.5px;
    color: var(--text-dark);
  }
  .person {
    position: absolute;
    left: 48px;
    width: 300px;
    top: 284px;
    text-align: center;
  }
  .person-name {
    font-size: 34px;
    color: var(--text-dark);
    line-height: 1;
  }
  .person-title {
    font-size: 20px;
    color: var(--text-soft);
    margin-top: 2px;
  }
  .divider {
    position: absolute;
    left: 366px;
    top: 263px;
    width: 2px;
    height: 107px;
    background: var(--divider);
  }
  .contacts {
    position: absolute;
    left: 391px;
    top: 270px;
    margin: 0;
    padding: 0;
    list-style: none;
  }
  .contact {
    display: flex;
    align-items: center;
    height: 31px;
    font-size: 18px;
    color: var(--text-dark);
  }
  .contact svg {
    width: 18px;
    height: 18px;
    margin-right: 11px;
    fill: none;
    stroke: var(--text-dark);
    stroke-width: 1.4;
  }
  .contact svg.solid {
    fill: var(--text-dark);
    stroke: none;
  }
  .web-band {
    position: absolute;
    left: 0;
    right: 0;
    bottom: 0;
    height: 58px;
    background: var(--brand-blue);
    color: var(--white);
    font-size: 20px;
    letter-spacing: 1px;
    display: flex;
    align-items: center;
    justify-content: center;
  }

  /* Stand-alone brand lockup */
  .lockup {
    position: absolute;
    left: 72px;
    top: 850px;
    display: flex;
    align-items: center;
    gap: 12px;
  }
  .lockup .brand-mark {
    width: 22px;
    height: 22px;
  }
  .lockup .brand-name {
    font-size: 32px;
  }
</style>
</head>
<body>
<main class="canvas">
  <section class="card" aria-label="Business card front">
    <div class="brand">
      <span class="brand-mark"></span>
      <span class="brand-name">Venkell Realtors</span>
    </div>
    <div class="rule"></div>
    <p class="address">Broker 5146 Marrow Ave. #327, Elmhaven, CA 91708</p>

    <div class="person">
      <div class="person-name">Bernard Venkell</div>
      <div class="person-title">Managing Director</div>
    </div>

    <div class="divider"></div>

    <ul class="contacts">
      <li class="contact">
        <svg viewBox="0 0 18 18" aria-hidden="true"><rect x="1.5" y="4" width="15" height="10"/><path d="M1.5 4 L9 10 L16.5 4"/></svg>
        bernard@venkellrealtors.com
      </li>
      <li class="contact">
        <svg viewBox="0 0 18 18" aria-hidden="true"><rect x="5" y="2" width="8" height="14" rx="1"/><rect x="6.5" y="4" width="5" height="5"/><line x1="8" y1="0.5" x2="8" y2="2"/></svg>
        +000 00 000 0000
      </li>
      <li class="contact">
        <svg class="solid" viewBox="0 0 18 18" aria-hidden="true"><path d="M2 6 Q9 1 16 6 L14 8 L12 6.5 L6 6.5 L4 8 Z"/><path d="M5 9 L13 9 L15 15 L3 15 Z"/></svg>
        +000 0 000 0000
      </li>
    </ul>

    <div class="web-band">www.bernardvenkellrealtors.com</div>
  </section>

  <div class="lockup">
    <span class="brand-mark"></span>
    <span class="brand-name">Venkell Realtors</span>
  </div>
</main>
</body>
</html>
```